2020 Binder Cover

Binder Design (front, spine, back) for a data analysis report in the education field. We provide a large binder full of in depth analyzed data. Design should mesh well with our 2020 report color pallet which is attached. The cover should allow for the title to be changed per Client. There is a cover example attached to give a better idea. The cover will be used with all of our clients with the name of their school district being changed for their specific report. The cover should communicate data and informed strategy for improvement and growth.

```html
<!DOCTYPE html>
<html lang="en">
<head>
<meta charset="utf-8">
<title>2020 Binder Cover – Front, Back and Spine</title>
<link href="https://fonts.googleapis.com/css2?family=Montserrat:wght@300;500;700;800&display=swap" rel="stylesheet">
<style>
  :root {
    --backdrop: #5fb6dd;
    --paper: #ffffff;
    --ink: #3a3a3a;
    --blue: #1f6aa5;
    --navy: #2c4f8a;
    --yellow: #f7df7e;
    --red: #d0264a;
    --plum: #5a3a73;
    --teal: #5e9196;
    --coral: #e2644f;
    --olive: #b6bb88;
  }
  * { box-sizing: border-box; margin: 0; padding: 0; }
  html, body { width: 849px; height: 1200px; overflow: hidden; }
  body {
    background: var(--backdrop);
    font-family: "Montserrat", sans-serif;
    color: var(--ink);
    position: relative;
  }
  .panel { position: absolute; background: var(--paper); overflow: hidden; }
  .pattern { position: absolute; left: 0; width: 100%; }
  .pattern--rows {
    background: linear-gradient(135deg,
      var(--teal) 0%, var(--blue) 14%, var(--yellow) 24%, var(--red) 34%,
      var(--plum) 46%, var(--olive) 56%, var(--blue) 66%, var(--coral) 78%,
      var(--navy) 88%, var(--yellow) 100%);
  }
  .pattern--columns {
    background: linear-gradient(90deg,
      var(--yellow) 0%, var(--blue) 10%, var(--red) 20%, var(--teal) 30%,
      var(--plum) 40%, var(--coral) 50%, var(--blue) 60%, var(--olive) 70%,
      var(--red) 80%, var(--navy) 90%, var(--yellow) 100%);
  }

  /* Front cover */
  .front { left: 40px; top: 133px; width: 375px; height: 528px; }
  .front .pattern { top: 0; height: 310px; }
  .front__brand {
    position: absolute; top: 44px; left: 128px;
    display: flex; align-items: center; gap: 6px;
    color: var(--paper); font-weight: 700; font-size: 15px;
  }
  .brand-dot { width: 14px; height: 14px; border-radius: 50%; background: currentColor; }
  .front__year {
    position: absolute; left: 18px; top: 191px;
    font-size: 128px; font-weight: 800; line-height: 1;
    color: var(--paper); letter-spacing: -4px;
  }
  .front__client { position: absolute; left: 24px; top: 318px; line-height: 1; }
  .front__client-name { display: block; font-size: 50px; font-weight: 800; }
  .front__client-type { display: block; font-size: 34px; font-weight: 800; margin-top: 4px; }
  .front__report { position: absolute; left: 26px; top: 444px; line-height: 1; }
  .front__report-kicker { display: block; font-size: 19px; font-weight: 300; }
  .front__report-title { display: block; font-size: 38px; font-weight: 700; margin-top: 1px; }

  /* Back cover */
  .back { left: 434px; top: 133px; width: 375px; height: 528px; }
  .back .pattern--upper { top: 0; height: 225px; }
  .back .pattern--lower { top: 337px; height: 191px; }
  .back__band {
    position: absolute; top: 225px; left: 0; width: 100%; height: 112px;
    text-align: center; padding-top: 22px;
  }
  .back__brand {
    display: inline-flex; align-items: center; gap: 5px;
    font-size: 12px; font-weight: 500;
  }
  .back__brand .brand-dot { width: 10px; height: 10px; }
  .back__address {
    font-style: normal; font-size: 7.5px; font-weight: 700; line-height: 1.45;
    margin-top: 14px;
  }

  /* Spine */
  .spine { left: 155px; top: 681px; width: 540px; height: 385px; }
  .spine .pattern { top: 0; height: 240px; }
  .spine__brand {
    position: absolute; left: 30px; top: 80px;
    transform-origin: left top; transform: rotate(90deg) translateY(-22px);
    display: flex; align-items: center; gap: 5px;
    color: var(--paper); font-size: 11px; font-weight: 500; white-space: nowrap;
  }
  .spine__brand .brand-dot { width: 9px; height: 9px; }
  .spine__title {
    position: absolute; top: 285px; left: 0; width: 100%;
    text-align: center; line-height: 1.25;
  }
  .spine__client { display: block; font-size: 20px; font-weight: 800; }
  .spine__report { display: block; font-size: 20px; font-weight: 300; }
</style>
</head>
<body>

  <section class="panel front" aria-label="Front cover">
    <div class="pattern pattern--rows" role="img" aria-label="Pattern of horizontal coloured data blocks in blue, yellow, red, purple, teal, coral and olive"></div>
    <div class="front__brand"><span class="brand-dot"></span>Brightpath Insights, LLC</div>
    <div class="front__year">2020</div>
    <h1 class="front__client">
      <span class="front__client-name">HARLOW</span>
      <span class="front__client-type">SCHOOL DISTRICT</span>
    </h1>
    <h2 class="front__report">
      <span class="front__report-kicker">COMPREHENSIVE NEEDS</span>
      <span class="front__report-title">ASSESSMENT</span>
    </h2>
  </section>

  <section class="panel back" aria-label="Back cover">
    <div class="pattern pattern--rows pattern--upper" role="img" aria-label="Pattern of horizontal coloured data blocks"></div>
    <div class="back__band">
      <div class="back__brand"><span class="brand-dot"></span>Brightpath Insights, LLC</div>
      <address class="back__address">
        BRIGHTPATH INSIGHTS, LLC<br>
        4120 Maple Ridge Lane<br>
        Fairview, MS 38000<br>
        555.014.2290
      </address>
    </div>
    <div class="pattern pattern--rows pattern--lower" role="img" aria-label="Pattern of horizontal coloured data blocks"></div>
  </section>

  <section class="panel spine" aria-label="Spine">
    <div class="pattern pattern--columns" role="img" aria-label="Pattern of vertical coloured data blocks in blue, yellow, red, purple, teal and coral"></div>
    <div class="spine__brand"><span class="brand-dot"></span>Brightpath Insights, LLC</div>
    <div class="spine__title">
      <span class="spine__client">HARLOW COUNTY SCHOOL DISTRICT</span>
      <span class="spine__report">COMPREHENSIVE NEEDS ASSESMENT</span>
    </div>
  </section>

</body>
</html>
```